Flyer marketing document - Kessway LMR Engineering

We need a more modern version of a marketing flyer/ brochures for our business and service offering. I would like an overall business brochure, plus potentially some examples of specific parts of the business. The brochure attached provides a fairly detailed overview of the business. We need to extract what the core offering is and have the ability to sell to the market this offering, around the innovative design, engineering and manufacture of the equipment we offer.

```html
<!DOCTYPE html>
<html lang="en">
<head>
<meta charset="utf-8">
<title>Kessway LMR Engineering – Brochure Pages 05–06</title>
<link href="https://fonts.googleapis.com/css2?family=Lato:wght@300;400&family=Roboto+Condensed:wght@400&display=swap" rel="stylesheet">
<style>
  :root {
    --backdrop: #efeaf7;
    --page: #e4e7f3;
    --ink: #2b2b2b;
    --accent-red: #d42027;
    --band-dark: #262626;
    --band-grey: #5a5a5a;
    --white: #ffffff;
    --photo-yellow: linear-gradient(135deg, #f2c230, #d9a014 55%, #5b5b5b);
    --photo-sky: linear-gradient(160deg, #b9cbe0 0%, #d9c88a 35%, #e5b21b 60%, #505050 100%);
    --photo-dark: linear-gradient(135deg, #3a3a3a, #6b6b6b 50%, #c89a3a);
    --photo-orange: linear-gradient(180deg, #6f8a55 0%, #a79a7d 30%, #e8692a 55%, #3a3a3a 100%);
    --photo-bucket: linear-gradient(180deg, #8a8e95 0%, #ec6a24 35%, #f07b2e 70%, #4b4d52 100%);
  }
  * { box-sizing: border-box; margin: 0; padding: 0; }
  html, body { width: 1200px; height: 870px; overflow: hidden; }
  body { background: var(--backdrop); font-family: "Lato", sans-serif; color: var(--ink); position: relative; }

  .page { position: absolute; top: 25px; width: 540px; height: 762px; background: var(--page); overflow: hidden; }
  .page--05 { left: 44px; }
  .page--06 { left: 617px; }

  .page-number { position: absolute; top: 24px; font-family: "Roboto Condensed", sans-serif; font-size: 13px; color: var(--ink); }
  .page--05 .page-number { left: 22px; }
  .page--06 .page-number { left: 505px; }
  .page-rule { position: absolute; top: 32px; height: 1.5px; background: var(--accent-red); width: 172px; }
  .page--05 .page-rule { left: 58px; }
  .page--06 .page-rule { left: 309px; }

  .body-copy { position: absolute; font-weight: 300; font-size: 10.6px; line-height: 13px; }
  .body-copy p + p { margin-top: 6px; }
  .justified { text-align: justify; hyphens: manual; }

  .photo { position: absolute; }

  .footer-band { position: absolute; top: 712px; left: 0; width: 540px; height: 26px; }
  .footer-url { position: absolute; top: 719px; font-size: 8.4px; letter-spacing: 1.9px; color: var(--white); font-weight: 400; }
  .footer-url .domain { color: var(--accent-red); }
  .page--05 .footer-url { right: 55px; }
  .page--06 .footer-url { left: 61px; }
</style>
</head>
<body>

<section class="page page--05">
  <span class="page-number">05</span>
  <span class="page-rule"></span>

  <div class="body-copy justified" style="left:57px; top:100px; width:172px;">
    <p>Australian Standard Access to roof areas, folding steps to allow access to service areas of truck engine and system compartments</p>
    <p style="margin-top:6px;">Rigid water tanks with Safety Access platform for easy and safe mainte&shy;nance of the water tanker pumping ,spray systems, and electrical sys&shy;tems. Tank fully still fully raise-able using the existing hoist system inte&shy;grated with water tank operating</p>
    <p style="margin-top:10px;">All tanks available with basic spray equipment or Aquamist and Sprayline Ground speed and spot spray water truck systems.</p>
  </div>

  <div class="photo" role="img" aria-label="Yellow water truck with safety access stairs, fire monitor and extinguisher" style="left:248px; top:101px; width:237px; height:303px; background:var(--photo-sky);"></div>
  <div class="photo" role="img" aria-label="Yellow mining water truck parked in a workshop" style="left:58px; top:325px; width:171px; height:79px; background:var(--photo-yellow);"></div>
  <div class="photo" role="img" aria-label="Hydraulic return filter and hoses mounted on yellow truck body" style="left:56px; top:425px; width:177px; height:244px; background:var(--photo-yellow);"></div>
  <div class="photo" role="img" aria-label="Hydraulic manifold and control valving on yellow frame" style="left:248px; top:425px; width:117px; height:87px; background:var(--photo-yellow);"></div>
  <div class="photo" role="img" aria-label="Electrical control box with switches and cabling" style="left:376px; top:425px; width:110px; height:88px; background:var(--photo-dark);"></div>

  <div class="body-copy justified" style="left:256px; top:541px; width:231px;">
    <p>Hydraulic systems utilise return filters and specially designed manifolds and control valving to simplify machine circuitry and modifications required to the truck to allow its use as a water tanker. 30 years of experience with modifying earthmoving equipment for its use as water tankers, tool carriers etc is fully utilised to come up with the best modification procedure to suit each machine.</p>
  </div>

  <svg class="footer-band" viewBox="0 0 540 26" aria-hidden="true">
    <polygon points="30,0 51,0 37,26 16,26" fill="var(--accent-red)"/>
    <polygon points="60,0 68,0 54,26 46,26" fill="var(--band-grey)"/>
    <polygon points="70,0 512,0 498,26 56,26" fill="var(--band-dark)"/>
    <polygon points="516,0 524,0 510,26 502,26" fill="var(--band-grey)"/>
    <polygon points="527,0 545,0 531,26 513,26" fill="var(--accent-red)"/>
  </svg>
  <span class="footer-url">www.<span class="domain">kesswaylmrengineering</span>.com</span>
</section>

<section class="page page--06">
  <span class="page-rule"></span>
  <span class="page-number">06</span>

  <div class="body-copy justified" style="left:53px; top:99px; width:428px;">
    <p>Our expertise and experience is not limited to water tanks and service trucks, we can apply our experience and hands on approach to any engineering problem requiring a solution. Other products in our range include Ejector trays, Earthmoving Buckets and attachments.</p>
  </div>

  <div class="photo" role="img" aria-label="Orange articulated dump truck fitted with an ejector tray" style="left:53px; top:150px; width:428px; height:168px; background:var(--photo-orange);"></div>
  <p class="body-copy" style="left:53px; top:331px; width:440px;">We will access every request for equipment and give our best price and delivery every time</p>

  <div class="photo" role="img" aria-label="Large orange earthmoving excavator bucket in a workshop" style="left:53px; top:363px; width:428px; height:277px; background:var(--photo-bucket);"></div>
  <p class="body-copy" style="left:53px; top:659px; width:440px;">Our expertise and experience in the design of earthmoving attachments is second to none.</p>

  <svg class="footer-band" viewBox="0 0 540 26" aria-hidden="true">
    <polygon points="0,0 12,0 26,26 14,26" fill="var(--accent-red)"/>
    <polygon points="16,0 24,0 38,26 30,26" fill="var(--band-grey)"/>
    <polygon points="30,0 467,0 481,26 44,26" fill="var(--band-dark)"/>
    <polygon points="472,0 480,0 494,26 486,26" fill="var(--band-grey)"/>
    <polygon points="486,0 506,0 522,26 502,26" fill="var(--accent-red)"/>
  </svg>
  <span class="footer-url">www.<span class="domain">kesswaylmrengineering</span>.com</span>
</section>

</body>
</html>
```